Business card design for modern law firm

We need new business cards. Information about our law firm can be found at www.qrtl-recht.de. The business cards should include the information that we have offices in Berlin and Stuttgart. They should be customizable for all attorneys who are partially located in Berlin and partially in Stuttgart. Example of the information:
Jonas Ackermann
lawyer
Specialist lawyer for copyright and media law
Lindenweg 17, 70374 Stuttgart
ackermann@qrtl-recht.de
+49 711 483 15 260
www.qrtl-recht.de
It is important for us that we can edit the cards independently, i.e. exchange names and contact details.
In addition, a QR code for a VCard should be placed on the card.
The design of the old maps is attached; the new design should clearly distinguish itself from them. They should be more modern. The design is ideally based on the design of the website www.qrtl-recht.de.
Industry/Entity Type
Rechtsanwalt
Contact Information for Business Card
Siehe projektbeschreibung

```html
<!DOCTYPE html>
<html lang="de">
<head>
<meta charset="utf-8">
<title>qrtl Rechtsanwälte – Visitenkarte</title>
<link rel="stylesheet" href="https://fonts.googleapis.com/css2?family=Roboto+Slab:wght@400;500;600&family=Arimo:wght@400&display=swap">
<style>
  :root {
    --backdrop: #e4e4e4;
    --card: #2e2e2e;
    --accent: #95c93d;
    --ink: #f2f2f2;
    --code-fill: #f2f2f2;
  }
  * { margin: 0; padding: 0; box-sizing: border-box; }
  html, body { width: 1200px; height: 1200px; overflow: hidden; }
  body { background: var(--backdrop); position: relative; font-family: "Arimo", Arial, sans-serif; }

  .card {
    position: absolute;
    left: 256px;
    width: 688px;
    height: 394px;
    background: var(--card);
    color: var(--ink);
    overflow: hidden;
  }
  .card--front { top: 159px; }
  .card--back { top: 653px; }

  .firm-line {
    font-family: "Roboto Slab", Georgia, serif;
    text-transform: uppercase;
    white-space: nowrap;
  }
  .firm-line--main { color: var(--accent); font-size: 22px; letter-spacing: 0.17em; font-weight: 500; }
  .firm-line--sub { color: var(--ink); font-size: 17px; letter-spacing: 0.12em; font-weight: 600; }
  .firm-line--sub .legal-form { text-transform: none; font-size: 15px; letter-spacing: 0.06em; }

  .front__firm { position: absolute; left: 43px; top: 47px; }
  .front__firm .firm-line--sub { margin-top: 8px; }

  .person { position: absolute; left: 43px; top: 143px; }
  .person__name { font-family: "Roboto Slab", Georgia, serif; color: var(--accent); font-size: 25px; font-weight: 500; line-height: 1.2; }
  .person__role { font-size: 15px; line-height: 19px; margin-top: 2px; }

  .address { position: absolute; left: 43px; top: 236px; font-size: 15.5px; line-height: 21px; font-style: normal; }

  .contact { position: absolute; left: 43px; top: 290px; list-style: none; font-size: 16px; }
  .contact li { display: flex; align-items: center; height: 20.5px; white-space: nowrap; }
  .contact svg { width: 13px; height: 13px; margin-right: 14px; fill: var(--accent); flex: none; }

  .wordmark {
    font-family: "Roboto Slab", Georgia, serif;
    color: var(--accent);
    font-weight: 400;
    line-height: 1;
    white-space: nowrap;
  }
  .front__wordmark { position: absolute; right: 34px; top: 150px; font-size: 180px; }

  .back__lockup { position: absolute; left: 113px; top: 150px; display: flex; align-items: center; }
  .back__wordmark { font-size: 100px; margin-right: 22px; }
  .back__firm .firm-line--sub { margin-top: 8px; }

  .offices {
    position: absolute;
    left: 43px;
    bottom: 34px;
    font-family: "Roboto Slab", Georgia, serif;
    font-size: 13px;
    letter-spacing: 0.14em;
    text-transform: uppercase;
    color: var(--ink);
  }
  .offices .offices__label { color: var(--accent); margin-right: 8px; }

  .vcard-code {
    position: absolute;
    right: 34px;
    bottom: 30px;
    width: 78px;
    height: 78px;
    background: var(--code-fill);
  }
</style>
</head>
<body>
  <section class="card card--front">
    <div class="front__firm">
      <div class="firm-line firm-line--main">Rechtsanwälte</div>
      <div class="firm-line firm-line--sub">Legal Services <span class="legal-form">PartmbB</span></div>
    </div>

    <div class="person">
      <div class="person__name">Jonas Ackermann</div>
      <div class="person__role">Specialist lawyer for<br>copyright &amp; media law</div>
    </div>

    <address class="address">Lindenweg 17<br>70374 Stuttgart</address>

    <ul class="contact">
      <li><svg viewBox="0 0 16 16" aria-hidden="true"><path d="M3.6 1.2l2.2 2.9c.3.4.2.9-.1 1.2L4.6 6.4c.8 2 2.6 3.8 4.9 4.9l1.1-1.1c.3-.3.8-.4 1.2-.1l2.9 2.2c.4.3.5.9.1 1.3l-1.4 1.4c-.6.6-1.500.8-2.3.5C6.3 13.9 2.1 9.7.6 4.9.3 4.1.5 3.2 1.1 2.6L2.3 1.1c.4-.4 1-.3 1.3.1z"/></svg>+49 711 483 15 260</li>
      <li><svg viewBox="0 0 16 16" aria-hidden="true"><path d="M0 3h16v1.2L8 9 0 4.2z M0 5.6l8 4.8 8-4.8V13H0z"/></svg>ackermann@qrtl-recht.de</li>
      <li><svg viewBox="0 0 16 16" aria-hidden="true"><path d="M8 0a8 8 0 100 16A8 8 0 008 0zm-1 2.5c.8.6 1.5 1.6 1.2 2.6-.3.9-1.6.8-2 1.7-.4.8.6 1.6.2 2.4-.4.7-1.5.5-2.1 1.1-.4.4-.4 1-.4 1.6A6 6 0 017 2.5zm3.5 10.8c-.2-.9.2-1.9 1-2.4.7-.5 1.9-.3 2.4-1a6 6 0 01-3.4 3.4z"/></svg>www.qrtl-recht.de</li>
    </ul>

    <div class="wordmark front__wordmark">qrtl</div>
  </section>

  <section class="card card--back">
    <div class="back__lockup">
      <div class="wordmark back__wordmark">qrtl</div>
      <div class="back__firm">
        <div class="firm-line firm-line--main">Rechtsanwälte</div>
        <div class="firm-line firm-line--sub">Legal Services <span class="legal-form">PartmbB</span></div>
      </div>
    </div>

    <div class="offices"><span class="offices__label">Standorte</span>Berlin · Stuttgart</div>

    <div class="vcard-code" role="img" aria-label="vCard QR code for the lawyer's contact details"></div>
  </section>
</body>
</html>
```